Retractable Banner Design for a GRC Software Product in Healthcare domain

We want a banner for branding and product positioning, in conferences and stalls. The stall's objective is to generate interest in the product, understand the market better, get feedback on the offering and to create customer engagements.

The banner should encourage visitors to drop by our stalls seeking more information about our product offering.

Target Market(s)

Asia

Industry/Entity Type

Healthcare

Requirements
Must have
• Product Logo, Tagline - "Patient Safety Solutions For Every Hospital", Visual indicators for Secure Software, Ease of use and Mobile responsive nature, Indicate availability of two flagship modules - Event Ledger and Care Progress Console
• QR Code link to the website.
Nice to have
• Module 1-line descriptions:
• Event Ledger: Make Incident reporting easy, meaningful and secure.
• Care Progress Console: Driver quality improvement efforts in healthcare.
• Relevant background pictures and/or graphics. We can provide 2-3 charts and/or screenshots if they would be more meaningful.
Should not have
• Should not be verbose.

```html
<!DOCTYPE html>
<html lang="en">
<head>
<meta charset="utf-8">
<title>PELIORA Roll-up Banner</title>
<link href="https://fonts.googleapis.com/css2?family=Montserrat:wght@500;600;700;800&display=swap" rel="stylesheet">
<style>
  :root {
    --brand-green: #11733a;
    --band-green: #138a3e;
    --band-green-dark: #0d6a31;
    --brand-red: #e0262f;
    --red-dark: #b21d27;
    --ink: #1a1a1a;
    --stage: #e4e4e4;
    --white: #ffffff;
  }
  * { margin: 0; padding: 0; box-sizing: border-box; }
  html, body { width: 1094px; height: 1200px; overflow: hidden; }
  body {
    background: var(--stage);
    font-family: "Montserrat", Arial, sans-serif;
    position: relative;
  }
  .banner {
    position: absolute;
    left: 307px; top: 15px;
    width: 480px; height: 1170px;
    background: var(--white);
    overflow: hidden;
  }
  .brand-name {
    position: absolute;
    top: 52px; left: 0; width: 100%;
    text-align: center;
    font-size: 66px; font-weight: 800;
    letter-spacing: 2px;
    color: var(--brand-green);
    line-height: 1;
  }
  .hero-visual {
    position: absolute;
    top: 144px; left: 0; width: 480px; height: 360px;
    background:
      radial-gradient(ellipse 45% 55% at 50% 45%, #2f9e4d 0%, #1f7f3c 45%, rgba(160,170,165,0) 80%),
      linear-gradient(180deg, #c9cdcb 0%, #aeb4b1 100%);
  }
  .hero-swoosh { position: absolute; top: 380px; left: 0; }
  .tagline {
    position: absolute;
    top: 512px; left: 67px;
    font-size: 34px; font-weight: 700;
    line-height: 40px;
    color: var(--brand-green);
    letter-spacing: 0.5px;
  }
  .feature-list { list-style: none; }
  .feature {
    position: absolute;
    left: 65px;
    display: flex; align-items: center;
    font-size: 25px; font-weight: 600;
    line-height: 24px;
    color: var(--ink);
  }
  .feature-icon {
    width: 38px; height: 38px; border-radius: 50%;
    background: var(--brand-red);
    box-shadow: 0 2px 3px rgba(0,0,0,0.3);
    display: flex; align-items: center; justify-content: center;
    margin-right: 20px; flex: none;
  }
  .modules-tab {
    position: absolute;
    top: 867px; left: 132px;
    width: 216px; height: 30px;
    z-index: 2;
  }
  .modules-tab span {
    position: absolute; inset: 0;
    text-align: center;
    line-height: 32px;
    font-size: 19px; font-weight: 500;
    color: var(--white);
  }
  .modules-band {
    position: absolute;
    top: 882px; left: 0; width: 480px; height: 180px;
    background: linear-gradient(90deg, var(--band-green-dark), var(--band-green) 50%, var(--band-green-dark));
    color: var(--white);
    text-align: center;
  }
  .module { position: absolute; left: 0; width: 100%; }
  .module-name { font-size: 17px; font-weight: 700; line-height: 22px; }
  .module-desc { font-size: 17px; font-weight: 500; line-height: 23px; }
  .module-divider {
    position: absolute; top: 99px; left: 65px; width: 346px; height: 1px;
    background: rgba(255,255,255,0.3);
  }
  .site-url {
    position: absolute;
    top: 1074px; left: 0; width: 100%;
    text-align: center;
    font-size: 29px; font-weight: 700;
    color: var(--brand-red);
  }
</style>
</head>
<body>
  <main class="banner">
    <div class="brand-name">PELIORA</div>

    <div class="hero-visual" role="img" aria-label="Person in green jacket holding a tablet with a ring of software-as-a-service icons around a central SaaS label"></div>
    <svg class="hero-swoosh" width="480" height="130" viewBox="0 0 480 130" aria-hidden="true">
      <polygon points="0,45 480,6 480,58 0,122" fill="var(--brand-red)"/>
      <polygon points="0,45 190,30 0,122" fill="var(--red-dark)"/>
      <polygon points="0,121 480,57 480,130 0,130" fill="var(--white)"/>
    </svg>

    <h1 class="tagline">PATIENT SAFETY<br>SOLUTIONS FOR<br>EVERY HOSPITAL</h1>

    <ul class="feature-list">
      <li class="feature" style="top:646px">
        <span class="feature-icon">
          <svg width="24" height="24" viewBox="0 0 24 24" fill="none" stroke="#fff" stroke-width="1.6" stroke-linecap="round"><path d="M6 16a4 4 0 0 1 0-8 5 5 0 0 1 9.6-1.2A4 4 0 0 1 18 16z"/><path d="M9 16v4M12 14v6M15 16v4"/></svg>
        </span>Secure SaaS Solution
      </li>
      <li class="feature" style="top:701px">
        <span class="feature-icon">
          <svg width="24" height="24" viewBox="0 0 24 24" fill="none" stroke="#fff" stroke-width="1.6"><rect x="3" y="4" width="15" height="11" rx="1"/><path d="M8 19h6M11 15v4"/><rect x="15" y="10" width="6" height="10" rx="1" fill="var(--brand-red)"/></svg>
        </span>Modern and<br>Mobile responsive
      </li>
      <li class="feature" style="top:762px">
        <span class="feature-icon">
          <svg width="24" height="24" viewBox="0 0 24 24" fill="none" stroke="#fff" stroke-width="1.6" stroke-linecap="round" stroke-linejoin="round"><path d="M10 13V5a1.5 1.5 0 0 1 3 0v6l4 1a2 2 0 0 1 1.5 2.3L17.5 20H10l-3-4a1.5 1.5 0 0 1 2.2-2z"/></svg>
        </span>Easy to use
      </li>
      <li class="feature" style="top:807px">
        <span class="feature-icon">
          <svg width="24" height="24" viewBox="0 0 24 24" fill="none" stroke="#fff" stroke-width="1.8" stroke-linejoin="round"><path d="M14 3 6 13h6l-2 8 8-10h-6z"/></svg>
        </span>Quick to deploy
      </li>
    </ul>

    <div class="modules-tab">
      <svg width="216" height="30" viewBox="0 0 216 30" aria-hidden="true">
        <defs><linearGradient id="tabShade" x1="0" y1="0" x2="0" y2="1"><stop offset="0" stop-color="#6a6a6a"/><stop offset="1" stop-color="#3a3a3a"/></linearGradient></defs>
        <polygon points="10,0 206,0 216,30 0,30" fill="url(#tabShade)"/>
      </svg>
      <span>Flagship Modules</span>
    </div>

    <section class="modules-band">
      <div class="module" style="top:24px">
        <div class="module-name">Event Ledger</div>
        <div class="module-desc">Make Incident reporting easy,<br>meaningful and secure.</div>
      </div>
      <div class="module-divider"></div>
      <div class="module" style="top:103px">
        <div class="module-name">Care Progress Console</div>
        <div class="module-desc">Driver quality improvement efforts<br>in healthcare.</div>
      </div>
    </section>

    <div class="site-url">www.carewardhq.com</div>
  </main>
</body>
</html>
```